Bright Path Trading
Business Cards and Stationary
Project: Bright Path Trading
Bright Path Trading -
Creative Brief
Modern
Rob and Kara Halvorsen, Owners
47 Elmcrest Road Larkfield, MA 01384
rob@brightpathtrading.com
www.brightpathtrading.com
Please put Kara's email underneath Rob's email: kara@brightpathtrading.com

```html
<!DOCTYPE html>
<html lang="en">
<head>
<meta charset="utf-8">
<title>Bright Path Trading – Business Card Concepts</title>
<link href="https://fonts.googleapis.com/css2?family=Cinzel:wght@400&family=PT+Sans:wght@400;700&display=swap" rel="stylesheet">
<style>
  :root {
    --page-bg: #ffffff;
    --label: #8a8a8a;
    --ink: #3a3a3a;
    --green: #7aa828;
    --green-dark: #4f8a1e;
    --rust: #b4471d;
    --grey-mark: #7b7b7b;
    --maroon-deep: #4a0606;
    --maroon: #8e1d12;
    --olive: #7d9a2a;
    --olive-light: #b2c454;
    --white: #ffffff;
  }
  * { box-sizing: border-box; margin: 0; padding: 0; }
  html, body { width: 1200px; height: 586px; overflow: hidden; background: var(--page-bg); }
  .sheet { position: relative; width: 1200px; height: 586px; }
  .label {
    position: absolute; width: 372px; text-align: center;
    font-family: "Cinzel", serif; font-size: 22px; letter-spacing: 1px;
    color: var(--label);
  }
  .card {
    position: absolute; width: 372px; height: 212px; overflow: hidden;
    box-shadow: 0 6px 10px -4px rgba(0,0,0,0.35);
    font-family: "PT Sans", sans-serif;
  }
  .col-1 { left: 20px; } .col-2 { left: 414px; } .col-3 { left: 808px; }
  .row-1-label { top: 18px; } .row-1 { top: 56px; }
  .row-2-label { top: 318px; } .row-2 { top: 356px; }

  /* front */
  .card-front { background: var(--white); }
  .band { position: absolute; left: 0; top: 0; width: 372px; height: 212px; }
  .brand { position: absolute; left: 14px; top: 16px; display: flex; align-items: center; gap: 6px; }
  .brand-dot { width: 12px; height: 12px; border-radius: 50%; }
  .brand-name { font-weight: 700; font-size: 19px; }
  .theme-green .brand-name { color: var(--green-dark); }
  .theme-green .brand-dot { background: var(--green-dark); }
  .theme-orange .brand-name { color: var(--rust); }
  .theme-orange .brand-dot { background: var(--rust); }
  .owners { position: absolute; left: 206px; top: 18px; color: var(--ink); }
  .owners-names { font-weight: 700; font-size: 13px; }
  .owners-title { font-size: 9px; margin-left: 90px; margin-top: 2px; }
  .contact {
    position: absolute; right: 14px; bottom: 14px; text-align: right;
    color: var(--white); font-size: 8.5px; line-height: 13px;
  }
  .contact .web { font-weight: 700; font-size: 9.5px; }

  /* back */
  .card-back { display: flex; align-items: center; justify-content: center; }
  .mark { display: flex; flex-direction: column; align-items: center; gap: 6px; }
  .mark-dot { width: 16px; height: 16px; border-radius: 50%; }
  .mark-name { font-weight: 700; font-size: 15px; }
  .back-grey { background: radial-gradient(circle at 50% 45%, #ffffff 0%, #e4e4e4 60%, #bfbfbf 100%); }
  .back-grey .mark-name { color: var(--grey-mark); } .back-grey .mark-dot { background: var(--grey-mark); }
  .back-maroon { background: radial-gradient(circle at 50% 45%, var(--maroon) 0%, #6a0f09 55%, var(--maroon-deep) 100%); }
  .back-maroon .mark-name { color: var(--white); } .back-maroon .mark-dot { background: var(--white); }
  .back-white { background: radial-gradient(circle at 50% 45%, #ffffff 0%, #f4f4f4 70%, #e2e2e2 100%); }
  .back-white .mark-name { color: var(--green); } .back-white .mark-dot { background: var(--green); }
  .back-olive { background: radial-gradient(circle at 50% 45%, var(--olive-light) 0%, #9bb23f 55%, var(--olive) 100%); }
  .back-olive .mark-name { color: var(--white); } .back-olive .mark-dot { background: var(--white); }
</style>
</head>
<body>
<div class="sheet">
  <div class="label col-1 row-1-label">FRONT</div>
  <div class="label col-2 row-1-label">BACK</div>
  <div class="label col-3 row-1-label">BACK</div>
  <div class="label col-1 row-2-label">FRONT</div>
  <div class="label col-2 row-2-label">BACK</div>
  <div class="label col-3 row-2-label">BACK</div>

  <svg width="0" height="0" style="position:absolute">
    <defs>
      <linearGradient id="band-green" x1="0" y1="0" x2="1" y2="0">
        <stop offset="0" stop-color="#5f9a22"/>
        <stop offset="1" stop-color="#c9da3c"/>
      </linearGradient>
      <linearGradient id="band-orange" x1="0" y1="0" x2="1" y2="0">
        <stop offset="0" stop-color="#e8812c"/>
        <stop offset="1" stop-color="#a8401b"/>
      </linearGradient>
    </defs>
  </svg>

  <!-- Row 1 -->
  <div class="card card-front theme-green col-1 row-1">
    <svg class="band" viewBox="0 0 372 212" aria-hidden="true">
      <path fill="url(#band-green)" d="M0,212 L0,122 C10,104 30,104 40,116 C52,100 80,100 90,114 C100,96 130,98 138,112 C150,124 165,124 175,112 C188,98 215,100 222,114 C235,126 250,124 258,112 C272,100 300,104 306,118 C318,108 340,108 350,120 C358,112 368,112 372,116 L372,212 Z"/>
    </svg>
    <div class="brand"><span class="brand-dot"></span><span class="brand-name">Bright Path Trading</span></div>
    <div class="owners"><div class="owners-names">Rob and Kara Halvorsen</div><div class="owners-title">Owners</div></div>
    <div class="contact">
      <div>47 Elmcrest Road Larkfield, NH 01384</div>
      <div>P: 555.201.4418 | F: 555.201.4419</div>
      <div>rob@brightpathtrading.com | kara@brightpathtrading.com</div>
      <div class="web">www.brightpathtrading.com</div>
    </div>
  </div>
  <div class="card card-back back-grey col-2 row-1">
    <div class="mark"><span class="mark-dot"></span><span class="mark-name">Bright Path Trading</span></div>
  </div>
  <div class="card card-back back-maroon col-3 row-1">
    <div class="mark"><span class="mark-dot"></span><span class="mark-name">Bright Path Trading</span></div>
  </div>

  <!-- Row 2 -->
  <div class="card card-front theme-orange col-1 row-2">
    <svg class="band" viewBox="0 0 372 212" aria-hidden="true">
      <path fill="url(#band-orange)" d="M0,212 L0,122 C10,104 30,104 40,116 C52,100 80,100 90,114 C100,96 130,98 138,112 C150,124 165,124 175,112 C188,98 215,100 222,114 C235,126 250,124 258,112 C272,100 300,104 306,118 C318,108 340,108 350,120 C358,112 368,112 372,116 L372,212 Z"/>
    </svg>
    <div class="brand"><span class="brand-dot"></span><span class="brand-name">Bright Path Trading</span></div>
    <div class="owners"><div class="owners-names">Rob and Kara Halvorsen</div><div class="owners-title">Owners</div></div>
    <div class="contact">
      <div>47 Elmcrest Road Larkfield, NH 01384</div>
      <div>P: 555.201.4418 | F: 555.201.4419</div>
      <div>rob@brightpathtrading.com | kara@brightpathtrading.com</div>
      <div class="web">www.brightpathtrading.com</div>
    </div>
  </div>
  <div class="card card-back back-white col-2 row-2">
    <div class="mark"><span class="mark-dot"></span><span class="mark-name">Bright Path Trading</span></div>
  </div>
  <div class="card card-back back-olive col-3 row-2">
    <div class="mark"><span class="mark-dot"></span><span class="mark-name">Bright Path Trading</span></div>
  </div>
</div>
</body>
</html>
```